Mouse and Rodent Infestation Spray

Need to Design label for 16oz bottle. The image sent has our initial design on it. Need other options.

Industry/Entity Type

Pest Control

Colors

Designer to choose colors to be used in the design.

```html
<!DOCTYPE html>
<html lang="en">
<head>
<meta charset="utf-8">
<title>Mouse &amp; Rodent Infestation Spray – 16 oz Label, Option B</title>
<link rel="stylesheet" href="https://fonts.googleapis.com/css2?family=Montserrat:wght@800;900&family=Barlow:wght@400;500&family=Barlow+Condensed:wght@600;700&display=swap">
<style>
  :root {
    --brand-red: #b3000c;
    --deep-red: #7d0008;
    --charcoal: #1c1c1e;
    --ink: #151515;
    --paper: #ffffff;
    --canvas: #ececec;
    --mist: #e4e4e4;
    --badge-blue: #2e86c9;
    --badge-green: #6cb33f;
    --badge-gold: #c9a227;
  }
  * { margin: 0; padding: 0; box-sizing: border-box; }
  html, body {
    width: 1200px; height: 1200px; overflow: hidden;
    background: var(--canvas);
  }
  .label {
    position: absolute; left: 60px; top: 60px;
    width: 1080px; height: 1080px;
    background: var(--paper);
    box-shadow: 0 3px 10px rgba(0,0,0,.18);
    display: flex; flex-direction: column;
    overflow: hidden;
  }

  /* Brand bar */
  .brand-bar {
    height: 120px; flex: none;
    background: var(--charcoal);
    display: flex; align-items: center; gap: 20px;
    padding: 0 56px;
  }
  .brand-mark { width: 34px; height: 34px; background: var(--brand-red); flex: none; }
  .brand-name {
    color: var(--paper);
    font-family: "Montserrat", sans-serif; font-weight: 800;
    font-size: 56px; letter-spacing: 10px; line-height: 1;
  }

  /* Hero: title and artwork */
  .hero {
    height: 400px; flex: none;
    display: flex; justify-content: space-between; align-items: center;
    padding: 0 56px;
  }
  .title { display: flex; flex-direction: column; }
  .title-red {
    color: var(--brand-red);
    font-family: "Montserrat", sans-serif; font-weight: 900;
    font-size: 112px; line-height: 1.02; letter-spacing: -1px; white-space: nowrap;
  }
  .title-red .amp { font-size: 84px; }
  .title-infestation {
    margin-top: 10px;
    color: var(--ink);
    font-family: "Barlow", sans-serif; font-weight: 500;
    font-size: 90px; line-height: 1; letter-spacing: 2px; white-space: nowrap;
  }
  .rodent-art {
    width: 280px; height: 280px; flex: none; border-radius: 50%;
    background: radial-gradient(circle at 50% 50%, #cfcfcf 0%, var(--mist) 60%, #f3f3f3 100%);
    box-shadow: inset 0 0 0 16px var(--brand-red);
  }

  /* Product type row */
  .type-row {
    height: 96px; flex: none;
    display: flex; align-items: center; gap: 28px;
    padding: 0 56px;
    border-top: 8px solid var(--brand-red);
  }
  .spray-pill {
    background: var(--brand-red); color: var(--paper);
    font-family: "Barlow", sans-serif; font-weight: 500;
    font-size: 50px; line-height: 66px; letter-spacing: 3px;
    padding: 0 28px; border-radius: 0 0 26px 0;
  }
  .use-note {
    font-family: "Barlow Condensed", sans-serif; font-weight: 700;
    font-size: 32px; color: var(--ink); letter-spacing: .5px; white-space: nowrap;
  }

  /* Details */
  .details {
    height: 190px; flex: none;
    display: grid; grid-template-columns: 1fr 1fr; column-gap: 40px;
    padding: 22px 56px 0;
  }
  .benefits {
    list-style: none;
    font-family: "Barlow", sans-serif; font-size: 27px; line-height: 44px;
    color: var(--ink); letter-spacing: .5px;
  }
  .benefits li { display: flex; align-items: center; gap: 14px; white-space: nowrap; }
  .benefits svg { width: 28px; height: 28px; flex: none; }
  .ingredients {
    border-left: 4px solid var(--brand-red); padding-left: 24px;
    font-family: "Barlow", sans-serif; font-size: 27px; line-height: 40px;
    color: var(--ink); letter-spacing: .5px;
  }
  .ingredients h3 {
    color: var(--brand-red);
    font-family: "Barlow Condensed", sans-serif; font-weight: 700;
    font-size: 32px; line-height: 44px; letter-spacing: .5px;
  }

  /* Volume */
  .volume-row {
    height: 124px; flex: none;
    display: flex; align-items: center;
    padding: 0 56px;
  }
  .volume {
    color: var(--brand-red);
    font-family: "Barlow Condensed", sans-serif; font-weight: 600;
    font-size: 64px; line-height: 1; white-space: nowrap;
  }

  /* Footer strip */
  .footer-strip {
    flex: 1;
    background: linear-gradient(90deg, var(--deep-red), var(--brand-red));
    display: flex; justify-content: space-between; align-items: center;
    padding: 0 56px;
  }
  .badges { display: flex; align-items: center; gap: 24px; }
  .badge { flex: none; }
  .badge-blue { width: 64px; height: 96px; border-radius: 12px; background: var(--badge-blue); }
  .badge-green { width: 74px; height: 96px; border-radius: 10px 10px 22px 22px; background: var(--badge-green); }
  .badge-gold { width: 84px; height: 84px; border-radius: 50%; background: var(--badge-gold); }
  .formula {
    color: var(--paper);
    font-family: "Barlow Condensed", sans-serif; font-weight: 700;
    font-size: 40px; line-height: 1; letter-spacing: 2px;
    border: 3px solid var(--paper); padding: 14px 26px; white-space: nowrap;
  }
</style>
</head>
<body>
  <div class="label">
    <header class="brand-bar">
      <span class="brand-mark"></span>
      <span class="brand-name">VERMORA</span>
    </header>

    <section class="hero">
      <div class="title">
        <span class="title-red">MOUSE <span class="amp">&amp;</span></span>
        <span class="title-red">RODENT</span>
        <span class="title-infestation">INFESTATION</span>
      </div>
      <div class="rodent-art" role="img" aria-label="Sketched rodent inside a red prohibition ring"></div>
    </section>

    <section class="type-row">
      <span class="spray-pill">SPRAY</span>
      <span class="use-note">SAFE FOR INDOOR / OUTDOOR USE</span>
    </section>

    <section class="details">
      <ul class="benefits">
        <li><svg viewBox="0 0 28 28"><circle cx="13" cy="15" r="11" fill="none" stroke="#b3000c" stroke-width="2.6"/><path d="M8 14l5 5 13-15" fill="none" stroke="#b3000c" stroke-width="3.2"/></svg>LONG-LASTING CONTROL</li>
        <li><svg viewBox="0 0 28 28"><circle cx="13" cy="15" r="11" fill="none" stroke="#b3000c" stroke-width="2.6"/><path d="M8 14l5 5 13-15" fill="none" stroke="#b3000c" stroke-width="3.2"/></svg>FREE OF PESTICIDES</li>
        <li><svg viewBox="0 0 28 28"><circle cx="13" cy="15" r="11" fill="none" stroke="#b3000c" stroke-width="2.6"/><path d="M8 14l5 5 13-15" fill="none" stroke="#b3000c" stroke-width="3.2"/></svg>NATURAL BAIT</li>
      </ul>
      <div class="ingredients">
        <h3>ACTIVE INGREDIENTS:</h3>
        <p>48% PEPPERMINT OIL</p>
        <p>52% SMART INGREDIENTS</p>
      </div>
    </section>

    <section class="volume-row">
      <span class="volume">16 FL OZ | 473 mL</span>
    </section>

    <footer class="footer-strip">
      <div class="badges">
        <div class="badge badge-blue" role="img" aria-label="Safety standard certification badge"></div>
        <div class="badge badge-green" role="img" aria-label="Natural product badge"></div>
        <div class="badge badge-gold" role="img" aria-label="Guarantee seal"></div>
      </div>
      <span class="formula">ADVANCED FORMULA</span>
    </footer>
  </div>
</body>
</html>
```